brand new Logo and business card

Need a brand new simple logo and business card for my finance business, under business name Harbourline Lending Partners. xxxxxxxxxxxxxxxxxxxxxxxxxxxxxxxxxxxxxxxxxxxxxxxxxxxxxxxxxxxxxxxxxxxxxxxxxxxxxxxxxxxxxxxxxxxxxxxxxxxxxxxxxxxxxxxxxxxxxxxxxxxxxxxxxxxxxxxxxxxxxxxxxxxxxxxxxxxxxxxxxxxxxxxx

Target Market(s)

all

Industry/Entity Type

Finance

Contact Information for Business Card

Need a brand new simple logo and business card for my finance business, under business name Harbourline Lending Partners. xxxxxxxxxxxxxxxxxxxxxxxxxxxxxxxxxxxxxxxxxxxxxxxxxxxxxxxxxxxxxxxxxxxxxxxxxxxxxxxxxxxxxxxxxxxxxxxxxxxxxxxxxxxxxxxxxxxxxxxxxxxxxxxx

Logo Text

Harbourline Lending Partners Home Loans | Plant & Equipment | Automotive | Business & Commercial | Personal

Logo styles of interest
Wordmark Logo
Lettermark Logo
Font styles to use
Serif
Sans Serif

Requirements
Must have
• Colin Marsh Managing Director
• harbourlinelendingpartners.example.com.au
• colin@harbourlinelendingpartners.example.com.au
• 0400 555 129 8am-9pm 7 Days
Nice to have
• nothing here to add
Should not have
• physical address

```html
<!DOCTYPE html>
<html lang="en">
<head>
<meta charset="utf-8">
<title>Harbourline Lending Partners – Business Card</title>
<link rel="stylesheet" href="https://fonts.googleapis.com/css2?family=Carlito:wght@400;700&display=swap">
<style>
  :root {
    --page: #ffffff;
    --frame-grey: #8c8c8c;
    --frame-line: #1e1e1e;
    --sky-top: #a7cdf3;
    --sky-mid: #d3e3f2;
    --sky-low: #dcdfe3;
    --sky-warm: #f1e2b4;
    --ink: #2f3a48;
    --mark-silver: #d9dadb;
  }
  html, body {
    margin: 0;
    width: 1200px;
    height: 815px;
    overflow: hidden;
    background: var(--page);
  }
  .canvas {
    position: relative;
    width: 1200px;
    height: 815px;
  }
  .business-card {
    position: absolute;
    left: 113px;
    top: 157px;
    width: 959px;
    height: 461px;
  }
  .card-sky {
    position: absolute;
    left: 18px;
    top: 18px;
    right: 18px;
    bottom: 18px;
    background:
      radial-gradient(ellipse 260px 140px at 60px 330px, var(--sky-warm) 0%, rgba(241,226,180,0) 100%),
      linear-gradient(180deg, var(--sky-top) 0%, var(--sky-mid) 45%, var(--sky-low) 100%);
  }
  .card-frame {
    position: absolute;
    inset: 0;
  }
  .contact-details {
    position: absolute;
    left: 34px;
    top: 68px;
    margin: 0;
    padding: 0;
    list-style: none;
    font-family: "Carlito", "Calibri", sans-serif;
    font-weight: 700;
    font-size: 23.5px;
    line-height: 37px;
    color: var(--ink);
    white-space: nowrap;
  }
  .brand-mark {
    position: absolute;
    left: 550px;
    top: 60px;
    width: 320px;
    height: 345px;
    display: flex;
    flex-direction: column;
    align-items: center;
    justify-content: center;
    gap: 22px;
  }
  .brand-square {
    width: 150px;
    height: 150px;
    background: var(--mark-silver);
  }
  .brand-name {
    margin: 0;
    text-align: center;
    font-family: "Carlito", "Calibri", sans-serif;
    font-weight: 700;
    font-size: 28px;
    line-height: 32px;
    color: var(--ink);
  }
</style>
</head>
<body>
<main class="canvas">
  <section class="business-card">
    <div class="card-sky" role="img" aria-label="Soft painted sky background in pale blue and grey"></div>

    <svg class="card-frame" width="959" height="461" viewBox="0 0 959 461" aria-hidden="true">
      <path fill-rule="evenodd" fill="var(--frame-grey)"
            d="M0 0 H959 V461 H0 Z M18 18 V443 H941 V18 Z"/>
      <rect x="6" y="6" width="947" height="449" fill="none" stroke="var(--frame-line)" stroke-width="3"/>
    </svg>

    <ul class="contact-details">
      <li class="contact-name">Colin Marsh Managing Director</li>
      <li class="contact-web">harbourlinelendingpartners.example.com.au</li>
      <li class="contact-email">colin@harbourlinelendingpartners.example.com.au</li>
      <li class="contact-phone">0400 555 129 8am-9pm 7 Days</li>
    </ul>

    <div class="brand-mark">
      <div class="brand-square"></div>
      <p class="brand-name">Harbourline<br>Lending Partners</p>
    </div>
  </section>
</main>
</body>
</html>
```